Regional Showdown Flyer for Holiday Program

Need a one page flyer, can be back to front or one page, ensuring you can fit all information, colourful, aimed at a market of 8-13 year old boys and girls.
The flyer needs to be noticed, needs to have certain information on it and needs to be Autralian Rule Football orientated.
Have uploaded file so you can understand the style (not content), style of flyer I am looking at getting submitted.

Target Market(s)

8-13 year old boys and girls and their parents.

Requirements
Must have
• Regional Showdown Event
• Price for Regional Showdown Day will be $85
• Strictly Limited Places, only the best footballers should enter this challenge
• Inaugural event, be the first Regional Showdown Winner for your age!
• Do you love a challenge! Put yourself to the test!
• Are you up to it - Water Slide Goal Kicking Contest! The fastest kick in the West (tested by our very own speed gun)! Can you survive the Footy Titan Trail or Last One Standing Goal Kicking! These challenges are crazy are super fun!
• If you think you can deliver on the big stage then this is for YOU!
• All District age winners will receive prizes, awards and the adulation from all their peers!
• Year's 3-5 from 9am to 12pm
• Year's 6-8 from 1-4pm
• All challengers compete against their own age
• Lunch Provided
• Monday 16th April - Upper Tarrowby Regional Showdown Day at Tarrowby Oval
• Tuesday 17th April - North Tarrowby Regional Showdown Day at Kilmorna Reserve
• Wednesday 18th April - Yarlo Regional Showdown Day - Dunhaven Football Club
• Every Challenge Participant receives a District Football!
• Need to put all 3 District Football Logos on the bottom of the flyer, logos attached at bottom.
Nice to have
• Plenty of colour, if you can fit all information on one page that would be fine
Should not have
• Dull, boring, any footballs should be Aussie Rules footballs not NFL or soccer

```html
<!DOCTYPE html>
<html lang="en">
<head>
<meta charset="utf-8">
<title>Regional Showdown Flyer</title>
<link href="https://fonts.googleapis.com/css2?family=Lato:wght@400;700;900&display=swap" rel="stylesheet">
<style>
  :root{
    --stage:#1b1d20;
    --paper:#ffffff;
    --red:#c8141c;
    --red-dark:#9e0f15;
    --orange:#ef4a1c;
    --ink:#2b2b2b;
    --blue:#1f78c8;
    --sky:#8fd0f2;
    --band-top:#0f3a2c;
    --band-bottom:#1a5a9c;
  }
  *{margin:0;padding:0;box-sizing:border-box}
  html,body{width:1200px;height:848px;overflow:hidden;background:var(--stage)}
  body{font-family:'Lato',sans-serif;position:relative}
  .flyer{position:absolute;left:300px;top:0;width:600px;height:848px;background:var(--paper);overflow:hidden}
  .colour-tiles{position:absolute;right:0;top:0;width:300px;height:330px;
    background:linear-gradient(225deg,#e8262a 0%,#f6911e 25%,#5cc14a 45%,#2f8fdc 65%,#c04fd1 82%,rgba(255,255,255,0) 100%);
    opacity:.85;clip-path:polygon(25% 0,100% 0,100% 100%,60% 70%)}
  .headline{position:absolute;left:40px;top:70px;font-weight:900;line-height:1.05;color:var(--red)}
  .headline span{display:block;font-size:40px}
  .headline .event{color:var(--orange);font-size:46px;letter-spacing:1px}
  .red-band{position:absolute;left:0;top:250px;width:400px;height:112px;background:linear-gradient(180deg,var(--red),var(--red-dark));
    clip-path:polygon(0 0,92% 0,100% 50%,92% 100%,0 100%);color:#fff;padding:16px 40px 0 40px;font-size:15px;font-weight:700;line-height:1.4}
  .red-band p+p{margin-top:6px}
  .bubble{position:absolute;right:22px;top:300px;width:180px;height:140px;border-radius:22px;background:linear-gradient(135deg,var(--sky),var(--blue));padding:14px}
  .bubble-inner{width:100%;height:100%;background:#fff;border-radius:14px;display:flex;align-items:center;justify-content:center;text-align:center;
    color:var(--orange);font-weight:900;font-size:16px;line-height:1.15;padding:6px}
  .bubble-dot{position:absolute;right:190px;top:440px;width:16px;height:16px;border-radius:50%;background:var(--blue)}
  .challenges{position:absolute;left:40px;top:390px;width:360px;font-size:13px;color:var(--ink);line-height:1.35}
  .challenges h2{font-size:16px;font-weight:900;color:var(--red);margin-bottom:6px}
  .challenges ul{list-style:none}
  .challenges li{position:relative;padding-left:14px;margin-bottom:3px}
  .challenges li::before{content:"";position:absolute;left:0;top:6px;width:7px;height:7px;border-radius:50%;background:var(--red)}
  .prizes{font-size:15px;font-weight:900;color:var(--red);margin:10px 0 6px}
  .sessions{font-size:14px}
  .age-badge{position:absolute;right:24px;top:520px;width:178px;height:178px;border-radius:50%;border:10px solid var(--orange);background:#fff;
    display:flex;align-items:center;justify-content:center;text-align:center;color:var(--blue);font-weight:900;font-size:21px;line-height:1.1;z-index:2}
  .schedule-band{position:absolute;left:0;bottom:0;width:600px;height:190px;background:linear-gradient(160deg,var(--band-top) 0%,#0d1e2c 45%,var(--band-bottom) 100%);
    color:#fff;padding:64px 40px 0 40px;font-size:13px;line-height:1.55}
  .lunch-tab{position:absolute;left:0;top:16px;background:#fff;color:var(--red);font-weight:900;font-size:20px;padding:6px 40px;border-radius:0 24px 24px 0}
</style>
</head>
<body>
  <main class="flyer">
    <div class="colour-tiles" role="img" aria-label="Scattered glossy colour tiles in red, orange, green, blue and purple"></div>

    <h1 class="headline">
      <span>Price for Regional</span>
      <span class="event">SHOWDOWN</span>
      <span>Day will be $85</span>
    </h1>

    <section class="red-band">
      <p>Strictly Limited Places, only the best footballers should enter this challenge</p>
      <p>Inaugural event, be the first Regional Showdown Winner for your age!</p>
    </section>

    <aside class="bubble"><div class="bubble-inner">If you think you can deliver on the big stage then this is for YOU!</div></aside>
    <div class="bubble-dot"></div>

    <section class="challenges">
      <h2>Do you love a challenge! Put yourself to the test!</h2>
      <ul>
        <li>Are you up to it - Water Slide Goal Kicking Contest!</li>
        <li>The fastest kick in the West (tested by our very own speed gun)!</li>
        <li>Can you survive the Footy Titan Trail or Last One Standing Goal Kicking!</li>
        <li>These challenges are crazy are super fun!</li>
      </ul>
      <p class="prizes">All District age winners will receive prizes, awards and the adulation from all their peers!</p>
      <p class="sessions">Year's 3-5 from 9am to 12pm<br>Year's 6-8 from 1-4pm</p>
    </section>

    <div class="age-badge">All<br>Challengers<br>Compete Against<br>their own<br>age</div>

    <footer class="schedule-band">
      <div class="lunch-tab">LUNCH PROVIDED</div>
      <p>Monday 16th April - Upper Tarrowby Regional Showdown Day at Tarrowby Oval</p>
      <p>Tuesday 17th April - North Tarrowby Regional Showdown Day at Kilmorna Reserve</p>
      <p>Wednesday 18th April - Yarlo Regional Showdown Day - Dunhaven Football Club</p>
      <p>Every Challenge Participant receives a District Football!</p>
    </footer>
  </main>
</body>
</html>
```